Letterhead Design for Law Firm that Specializes in Property Damage Litigation

We are looking for a redesign of our letterhead. Our current letterhead lists all of our current staff members and we'd like to come up with a design that does NOT list all of the staff members so that it does not need to be updated with every newly hired employee. Must be in editable format.

We are a law firm that specializes in property damage, so we need something that is professional, yet modern. The final design should use our existing logo and should use a blue color scheme (alternate colors would be gray, black, and white).

Industry/Entity Type

Legal

Colors
0054AA
0677BA
7BADD7
CADEEF
E8F1F8

```html
<!DOCTYPE html>
<html lang="en">
<head>
<meta charset="utf-8">
<title>Hartwell Ames &amp; Corran — Letterhead</title>
<link href="https://fonts.googleapis.com/css2?family=Libre+Baskerville:wght@700&family=Open+Sans:wght@400;600;700&display=swap" rel="stylesheet">
<style>
  :root {
    --navy: #1b2a4a;
    --blue: #0054aa;
    --mid-blue: #0677ba;
    --sky: #7badd7;
    --pale: #cadeef;
    --mist: #e8f1f8;
    --gray: #8a8f98;
    --light-gray: #c9ccd1;
    --ink: #2b2f36;
    --paper: #ffffff;
    --backdrop: #dfe9f3;
  }
  * { margin: 0; padding: 0; box-sizing: border-box; }
  html, body { width: 1200px; height: 2688px; overflow: hidden; background: var(--backdrop); }
  body { font-family: "Open Sans", Arial, sans-serif; color: var(--ink); }

  .letterhead {
    position: absolute; left: 0; top: 316px;
    width: 1200px; height: 2056px;
    background: var(--paper); overflow: hidden;
  }
  .decor { position: absolute; left: 0; top: 0; width: 1200px; height: 2056px; }

  .firm { position: absolute; right: 40px; top: 150px; text-align: right; }
  .firm-name {
    display: flex; align-items: center; justify-content: flex-end; gap: 18px;
    font-family: "Libre Baskerville", Georgia, serif; font-weight: 700;
    color: var(--navy); font-size: 40px; line-height: 1.05; letter-spacing: 1px;
  }
  .firm-mark { width: 26px; height: 26px; background: var(--blue); flex: none; }
  .firm-tagline {
    margin-top: 22px; font-size: 21px; font-weight: 600; letter-spacing: 5px;
    color: var(--navy);
  }
  .firm-web { margin-top: 8px; font-size: 18px; letter-spacing: 6px; color: var(--gray); }

  .recipient { position: absolute; left: 100px; top: 418px; font-size: 18px; line-height: 26px; }
  .recipient strong { font-weight: 700; color: var(--navy); }
  .company { position: absolute; left: 100px; top: 556px; font-size: 18px; line-height: 28px; }
  .company strong { color: var(--navy); }
  .date { position: absolute; right: 40px; top: 628px; font-size: 18px; font-weight: 700; color: var(--navy); }

  .body-copy { position: absolute; left: 100px; top: 756px; width: 1060px; font-size: 19px; line-height: 29px; }
  .body-copy p { margin-bottom: 22px; }

  .signature { position: absolute; right: 40px; top: 1290px; text-align: right; }
  .signature-mark { display: block; width: 200px; height: 70px; margin-left: auto; background: linear-gradient(90deg, transparent, var(--light-gray)); }
  .signer { margin-top: 14px; font-size: 19px; font-weight: 700; color: var(--navy); }
  .signer-role { font-size: 16px; color: var(--gray); }

  .office { position: absolute; top: 1536px; font-size: 18px; line-height: 27px; color: var(--ink); }
  .office h3 { font-size: 18px; font-weight: 700; color: var(--blue); letter-spacing: 0.5px; }
  .office-pa { left: 150px; }
  .office-nj { left: 600px; }
  .office address { font-style: normal; margin-top: 48px; }
  .office-nj address { margin-top: 48px; }
</style>
</head>
<body>
<main class="letterhead">
  <svg class="decor" viewBox="0 0 1200 2056" aria-hidden="true">
    <!-- top-left diagonal bands -->
    <polygon points="0,40 60,0 110,0 0,90" fill="var(--light-gray)"/>
    <polygon points="0,120 150,20 150,60 0,180" fill="var(--navy)"/>
    <polygon points="0,210 120,130 120,190 0,280" fill="var(--blue)"/>
    <polygon points="0,300 90,240 90,280 0,340" fill="var(--sky)"/>
    <!-- left rule with contact icons -->
    <line x1="48" y1="400" x2="48" y2="1900" stroke="var(--blue)" stroke-width="3"/>
    <circle cx="58" cy="1600" r="26" fill="var(--paper)" stroke="var(--blue)" stroke-width="3"/>
    <path d="M49 1589 q-4 4 0 12 q6 10 16 16 q8 4 12 0 l-5 -6 q-3 2 -6 0 q-6 -4 -10 -10 q-2 -3 0 -6 z" fill="var(--blue)"/>
    <circle cx="58" cy="1712" r="26" fill="var(--paper)" stroke="var(--blue)" stroke-width="3"/>
    <path d="M58 1726 q-12 -14 -12 -22 a12 12 0 0 1 24 0 q0 8 -12 22 z" fill="var(--blue)"/>
    <circle cx="58" cy="1704" r="4" fill="var(--paper)"/>
    <!-- right footer bars -->
    <polygon points="1040,1820 1200,1820 1200,1850 1010,1850" fill="var(--light-gray)"/>
    <polygon points="980,1880 1200,1880 1200,1920 950,1920" fill="var(--blue)"/>
    <!-- bottom band -->
    <rect x="0" y="1968" width="1200" height="88" fill="var(--navy)"/>
    <polygon points="0,1940 260,1940 200,2056 0,2056" fill="var(--blue)"/>
    <polygon points="270,1968 330,1968 270,2056 210,2056" fill="var(--sky)"/>
    <polygon points="340,1968 370,1968 310,2056 280,2056" fill="var(--light-gray)"/>
  </svg>

  <header class="firm">
    <div class="firm-name"><span class="firm-mark"></span><span>HARTWELL<br>AMES &amp;<br>CORRAN</span></div>
    <div class="firm-tagline">THE PROPERTY DAMAGE ATTORNEYS</div>
    <div class="firm-web">www.hacpropertylaw.com</div>
  </header>

  <section class="recipient">
    <strong>TO</strong><br>
    <strong>THE RECIEVER</strong><br>
    Managing Director
  </section>
  <section class="company">
    <strong>Name of the Company</strong><br>
    Address of the company:<br>
    phone number:
  </section>
  <div class="date">Mar, 27th 2023</div>

  <article class="body-copy">
    <p>Dear Sir,</p>
    <p>I know it can be a rocky road to finding the right freelancer that...Has the skills you need, someone who understands the principles of creating designs that will attract your target audience, AND who is actually motivated to work closely with you, AND That you can trust to get the job done RIGHT, the FIRST time while following your brief. I made many variations of the logo ranging from colored to the black and white version, the app on, color variations, and logo formation variations, so that you can make choice.</p>
    <p>I made research about this project especially about the jet stream dynamics, at least I grabbed a bit of the normal west-to-east jet stream where it happens to be cold and the other side where it happens to be warm. And how does it apply to the logo, so in the color of the cloud in the logo icon which is bluish, I made it to be a darker blue flowing to a warm blue, the dark shade representing cold and warm shade representing warm.</p>
    <p>The concept is actually a bright sun coming out from the cloud, and the radial patterns represents Continuous revolving of the earth as related to weather, this is a also a radial pattern that symbolizes trust, unity and quality according to logo physiology.</p>
  </article>

  <section class="signature">
    <span class="signature-mark" role="img" aria-label="Handwritten signature"></span>
    <div class="signer">Daniel R. Foster</div>
    <div class="signer-role">Managing Director</div>
  </section>

  <section class="office office-pa">
    <h3>PHILADELPHIA OFFICE</h3>
    215.555.0140<br>215.555.0172
    <address>2200 Market Crossing<br>Suite 410<br>Philadelphia , Pa 19100</address>
  </section>
  <section class="office office-nj">
    <h3>NEW JERSEY OFFICE</h3>
    856.555.0193<br>215.555.0172
    <address>880 Orchard Lane North<br>Suite 120<br>Maple Grove, NJ 08000</address>
  </section>
</main>
</body>
</html>
```